Business Card & Stationary for Cleaning Company
Business Card, Letterhead, Invoice, Envelope, Fax Cover, Presentation Folder (Letter)
Professional
Brightwave Home Services
Maple Hollow and Surround Area
Name@brightwavehomeservices.example
www.brightwavehomeservices.example
Please integrate my already-completed company logo (attached) in a clean, modern design for business cards, Fax cover sheet, letterhead, envelopes, Invoice and Presentation Folder (Letter).
Here is my company logo in ai format. Please let me know if there's another format you prefer to work with; I'll try to send that along.
This project is a guaranteed as you can see the link below for the new logo.
http://www.pixelquarry.example/contests/a-logo-for-cleaning-company

```html
<!DOCTYPE html>
<html lang="en">
<head>
<meta charset="utf-8">
<title>Brightwave Home Services — Stationery Set</title>
<link rel="stylesheet" href="https://fonts.googleapis.com/css2?family=Arimo:wght@400;700&display=swap">
<style>
:root{
  --bg:#151618;
  --paper:#ffffff;
  --ink:#3a3d42;
  --muted:#8a9097;
  --rule:#d5d9de;
  --blue:#1f86c9;
  --blue-dark:#0c4f8f;
  --blue-light:#5fb6ea;
  --green:#7cc242;
  --green-dark:#4f9a2a;
  --faint:#eef2f6;
}
*{box-sizing:border-box;margin:0;padding:0}
html,body{width:1200px;height:899px;overflow:hidden;background:var(--bg);font-family:"Arimo",Arial,sans-serif;color:var(--ink)}
.canvas{position:relative;width:1200px;height:899px;background:linear-gradient(180deg,#1d1f22,#0e0f10)}
.sheet{position:absolute;background:var(--paper);overflow:hidden;box-shadow:0 4px 14px rgba(0,0,0,.6)}
.brand{display:flex;align-items:center;gap:6px;color:var(--blue);font-weight:700;line-height:1.1;white-space:nowrap}
.brand .dot{width:14px;height:14px;border-radius:50%;background:var(--blue);flex:none}
.brand span{font-size:13px}
.mark-faint{position:absolute;border-radius:50%;background:var(--faint)}
.footer-band{position:absolute;left:0;right:0;bottom:0;height:30px;background:linear-gradient(90deg,var(--blue-dark),var(--blue) 60%,var(--blue-light))}
.footer-band::before{content:"";position:absolute;left:0;right:0;top:-4px;height:4px;background:var(--green)}
.footer-band .web{position:absolute;left:16px;top:10px;color:#fff;font-size:8px;letter-spacing:1.5px;white-space:nowrap}
.footer-info{position:absolute;left:16px;bottom:40px;font-size:6px;color:var(--muted);white-space:nowrap}
.small{font-size:6.5px;line-height:1.55;color:var(--ink)}
/* letterhead */
.letterhead{left:12px;top:12px;width:389px;height:503px}
.letterhead .brand{position:absolute;left:26px;top:22px}
.letterhead .body{position:absolute;left:26px;top:92px;width:300px}
.letterhead .body p{margin-bottom:9px}
/* fax */
.fax{left:428px;top:12px;width:364px;height:503px}
.fax .brand{position:absolute;left:0;right:0;top:22px;justify-content:center}
.fax h1{position:absolute;left:26px;top:70px;font-size:40px;font-weight:400;letter-spacing:2px;color:#222}
.fax .fields{position:absolute;left:26px;top:125px;width:312px;display:grid;grid-template-columns:1fr 1fr;column-gap:14px;row-gap:8px}
.fax .field{display:flex;gap:6px;font-size:6.5px;border-bottom:1px solid var(--rule);padding-bottom:2px;white-space:nowrap}
.fax .field b{width:30px;flex:none}
.fax .checks{position:absolute;left:26px;top:242px;display:flex;gap:12px;font-size:6.5px;white-space:nowrap}
.fax .checks span{display:flex;align-items:center;gap:3px}
.fax .checks i{width:7px;height:7px;border:1px solid #555}
/* invoice */
.invoice{left:814px;top:12px;width:372px;height:503px}
.invoice .brand{position:absolute;left:22px;top:22px}
.invoice h1{position:absolute;left:22px;top:72px;font-size:17px;font-weight:700;color:#222;letter-spacing:.5px}
.invoice .meta{position:absolute;right:22px;top:74px;font-size:6px;text-align:right;color:var(--ink)}
.invoice table{position:absolute;left:22px;width:328px;border-collapse:collapse;font-size:5.5px}
.invoice th{background:var(--faint);text-align:left;padding:2px 3px;border:1px solid var(--rule);font-weight:700}
.invoice td{padding:2px 3px;border:1px solid var(--rule);height:10px}
.invoice .num{text-align:right}
/* envelope */
.envelope{left:12px;top:724px;width:195px;height:138px}
.envelope .brand span{font-size:9px}
.envelope .brand .dot{width:10px;height:10px}
.envelope .brand{position:absolute;left:10px;top:10px}
.envelope .window{position:absolute;left:72px;top:66px;width:110px;height:32px;border:1px solid #b9bec4;background:#f5f7f9;border-radius:3px}
.envelope .footer-band{height:14px}
.envelope .footer-band .web{top:4px;font-size:5px}
/* folder inside */
.folder-in{left:231px;top:547px;width:583px;height:315px;background:transparent;box-shadow:none;overflow:visible}
.folder-in .panel{position:absolute;top:0;width:291px;height:315px;background:var(--paper);box-shadow:0 4px 14px rgba(0,0,0,.6)}
.folder-in .left{left:0}
.folder-in .right{left:292px;overflow:hidden}
.card-white{position:absolute;left:6px;top:40px;width:140px;height:80px;background:#fff;border:1px solid var(--rule);box-shadow:0 2px 5px rgba(0,0,0,.25);padding:10px}
.card-white .brand span{font-size:8px}
.card-white .brand .dot{width:9px;height:9px}
.card-white .contact{position:absolute;right:10px;top:16px;font-size:5px;text-align:right;color:var(--ink);line-height:1.5}
.card-white .strip{position:absolute;left:0;right:0;bottom:0;height:8px;background:linear-gradient(90deg,var(--blue-dark),var(--blue))}
.card-blue{position:absolute;left:40px;top:60px;width:150px;height:86px;border-radius:3px;background:linear-gradient(135deg,var(--blue-light),var(--blue) 55%,var(--blue-dark));box-shadow:0 2px 5px rgba(0,0,0,.3);display:flex;align-items:center;justify-content:center}
.card-blue .brand{color:#fff}
.card-blue .brand .dot{background:#fff;width:10px;height:10px}
.card-blue .brand span{font-size:9px}
.pocket{position:absolute;left:0;bottom:0;width:291px;height:130px}
/* folder cover */
.folder-cover{left:838px;top:540px;width:348px;height:340px;background:linear-gradient(160deg,var(--blue-light),var(--blue) 45%,var(--blue-dark))}
.folder-cover .brand{position:absolute;left:0;right:0;top:96px;justify-content:center;color:#fff}
.folder-cover .brand .dot{background:#fff;width:18px;height:18px}
.folder-cover .brand span{font-size:18px}
.folder-cover .tag{position:absolute;left:0;right:0;top:126px;text-align:center;font-size:7px;color:#dbeefb;letter-spacing:1px}
.folder-cover .web{position:absolute;left:20px;bottom:16px;font-size:7px;color:#fff;letter-spacing:1px}
</style>
</head>
<body>
<div class="canvas">

  <section class="sheet letterhead" aria-label="Letterhead">
    <div class="brand"><i class="dot"></i><span>Brightwave Home Services</span></div>
    <div class="mark-faint" style="right:20px;bottom:60px;width:120px;height:120px"></div>
    <div class="body small">
      <p>Recipient Name<br>Street Address<br>City, State Zip</p>
      <p>March 14, 2012</p>
      <p>Dear Client,</p>
      <p>Thank you for choosing our team for your home and office cleaning needs. We are pleased to confirm the details of our service agreement and look forward to keeping your spaces fresh, bright and welcoming every week.</p>
      <p>Our trained crew uses safe, eco friendly products and careful methods on every surface. Each visit follows a checklist so nothing is missed, and your feedback helps us improve.</p>
      <p>Please review the enclosed schedule and contact us with any questions about timing, rooms or special requests.</p>
      <p>We value your trust and your time.</p>
      <p>Yours sincerely,<br><br>Name Surname</p>
    </div>
    <div class="footer-info">Maple Hollow · Phone 919 555 0142 · Fax 919 555 0143 · Name@brightwavehomeservices.example</div>
    <div class="footer-band"><span class="web">www.brightwavehomeservices.example</span></div>
  </section>

  <section class="sheet fax" aria-label="Fax cover sheet">
    <div class="brand"><i class="dot"></i><span>Brightwave Home Services</span></div>
    <h1>FAX</h1>
    <div class="fields">
      <div class="field"><b>To:</b>[Type the recipient name]</div>
      <div class="field"><b>From:</b>[Type your name]</div>
      <div class="field"><b>Fax:</b>[Type the fax number]</div>
      <div class="field"><b>Pages:</b>[Number of pages]</div>
      <div class="field"><b>Phone:</b>[Type the phone number]</div>
      <div class="field"><b>Date:</b>[Pick the date]</div>
      <div class="field"><b>Re:</b>[Type the subject]</div>
      <div class="field"><b>CC:</b>[Type text]</div>
    </div>
    <div class="checks">
      <span><i></i>Urgent</span><span><i></i>For Review</span><span><i></i>Please Comment</span><span><i></i>Please Reply</span><span><i></i>Please Recycle</span>
    </div>
    <div class="mark-faint" style="right:20px;bottom:60px;width:120px;height:120px"></div>
    <div class="footer-info">Maple Hollow · Phone 919 555 0142 · Fax 919 555 0143</div>
    <div class="footer-band"><span class="web">www.brightwavehomeservices.example</span></div>
  </section>

  <section class="sheet invoice" aria-label="Proforma invoice">
    <div class="brand"><i class="dot"></i><span>Brightwave Home Services</span></div>
    <h1>PROFORMA INVOICE</h1>
    <div class="meta">Date: March 14, 2012<br>Invoice No: BWH1987</div>
    <table style="top:104px">
      <tr><th>Shipper</th><th>Consignee</th></tr>
      <tr><td>Company Name<br>Street Address<br>City, State Zip</td><td>Client Name<br>Street Address<br>City, State Zip</td></tr>
    </table>
    <table style="top:160px">
      <tr><th>Reason for Export</th></tr>
      <tr><td>Cleaning supplies for scheduled service</td></tr>
    </table>
    <table style="top:196px">
      <tr><th>Mode of Transport</th><th>Total Number of Packages</th><th>Total Gross Weight</th></tr>
      <tr><td>Ground</td><td class="num">4</td><td class="num">22 lb</td></tr>
    </table>
    <table style="top:232px">
      <tr><th>Description</th><th>Quantity</th><th>Unit Price</th><th>Total</th></tr>
      <tr><td>Item 1 description</td><td class="num">2</td><td class="num">120.00</td><td class="num">240.00</td></tr>
      <tr><td>Item 2 description</td><td class="num">1</td><td class="num">95.00</td><td class="num">95.00</td></tr>
      <tr><td>Item 3 description</td><td class="num">3</td><td class="num">40.00</td><td class="num">120.00</td></tr>
      <tr><td>Item 4 description</td><td class="num">1</td><td class="num">60.00</td><td class="num">60.00</td></tr>
      <tr><td></td><td></td><td>Subtotal</td><td class="num">515.00</td></tr>
      <tr><td></td><td></td><td>Tax</td><td class="num">35.00</td></tr>
      <tr><td>Thank you for your business</td><td></td><td><b>Total</b></td><td class="num"><b>550.00</b></td></tr>
    </table>
    <div class="mark-faint" style="right:20px;bottom:60px;width:110px;height:110px"></div>
    <div class="footer-info">Maple Hollow · Phone 919 555 0142 · Fax 919 555 0143</div>
    <div class="footer-band"><span class="web">www.brightwavehomeservices.example</span></div>
  </section>

  <section class="sheet envelope" aria-label="Envelope">
    <div class="brand"><i class="dot"></i><span>Brightwave Home Services</span></div>
    <div class="window"></div>
    <div class="footer-band"><span class="web">www.brightwavehomeservices.example</span></div>
  </section>

  <section class="sheet folder-in" aria-label="Presentation folder inside with business cards">
    <div class="panel left">
      <div class="card-white">
        <div class="brand"><i class="dot"></i><span>Brightwave<br>Home Services</span></div>
        <div class="contact"><b>Name Surname</b><br>Position<br>919 555 0142<br>Name@brightwavehomeservices.example</div>
        <div class="strip"></div>
      </div>
    </div>
    <div class="panel right">
      <div class="card-blue"><div class="brand"><i class="dot"></i><span>Brightwave Home Services</span></div></div>
      <svg class="pocket" viewBox="0 0 291 130" preserveAspectRatio="none" aria-hidden="true">
        <path d="M0 40 C90 10 200 10 291 30 L291 130 L0 130 Z" fill="var(--green)"/>
        <path d="M0 58 C100 30 200 36 291 52 L291 130 L0 130 Z" fill="var(--green-dark)" opacity=".35"/>
        <path d="M0 40 C90 10 200 10 291 30" fill="none" stroke="#fff" stroke-width="2"/>
      </svg>
    </div>
  </section>

  <section class="sheet folder-cover" aria-label="Presentation folder cover">
    <svg style="position:absolute;inset:0" width="348" height="340" viewBox="0 0 348 340" aria-hidden="true">
      <path d="M348 20 C250 80 240 220 348 300 Z" fill="#ffffff" opacity=".12"/>
      <path d="M0 250 C120 210 240 230 348 200" fill="none" stroke="#ffffff" stroke-width="2" opacity=".35"/>
      <circle cx="270" cy="230" r="70" fill="#ffffff" opacity=".08"/>
    </svg>
    <div class="brand"><i class="dot"></i><span>Brightwave Home Services</span></div>
    <div class="tag">HOME AND OFFICE CARE</div>
    <div class="web">www.brightwavehomeservices.example</div>
  </section>

</div>
</body>
</html>
```